Redesign Of Current Landing Page

I need to redesign this landing page https://www.brightoakpromos.biz/?page=landing&landing=23 (Please do not opt in because when you do it will show you the home page. Please clear your cookies before going to this url above to view the 1 page landing page.)

Please use my updated website as a reference for colors and logo.
http://layoutcraftzone.com/dh/bopg/index.html

I would like the call to action to be a button that opens into a lead form...

Button would be "Download Samples"

small business owners

Marketing

1 page

Designer to choose colors to be used in the design.

• must be full responsive on all devices
• must have a legitimate professional apeal to it
• open

```html
<!DOCTYPE html>
<html lang="en">
<head>
<meta charset="utf-8">
<title>Bright Oak Promos – Attract More Customers</title>
<link rel="stylesheet" href="https://fonts.googleapis.com/css2?family=Raleway:wght@200;300;400;500;600;700;800&family=Oswald:wght@500&family=Open+Sans:wght@400;600&display=swap">
<style>
:root{
  --navy:#16202e;
  --navy-deep:#0f1722;
  --blue:#1570bf;
  --blue-light:#2f8fd6;
  --blue-dark:#0b4f91;
  --orange:#f2a20d;
  --orange-dark:#d98a00;
  --text:#333;
  --muted:#555;
  --light-bg:#f6f6f6;
  --white:#fff;
}
*{box-sizing:border-box;margin:0;padding:0}
html,body{width:1200px;height:2236px;overflow:hidden}
body{position:relative;font-family:"Raleway",Arial,sans-serif;color:var(--text);background:var(--white)}
a{text-decoration:none}
.abs{position:absolute}

/* header */
.topbar{left:0;top:0;width:1200px;height:57px;background:var(--navy)}
.brand{left:210px;top:15px;display:flex;align-items:center;gap:10px;color:var(--blue-light);font-weight:700;font-size:20px;letter-spacing:.5px}
.brand-mark{width:26px;height:26px;background:var(--blue-light);border-radius:50%}
.contact{left:812px;top:11px;display:flex;gap:10px;color:var(--white);font-size:12.5px;line-height:17px}
.contact strong{color:var(--blue-light);font-weight:700}

/* hero */
.hero{left:0;top:57px;width:1200px;height:443px;background:linear-gradient(180deg,#1d2c44 0%,#2d4666 45%,#1b2e48 100%)}
.hero-curve{left:0;top:440px;width:1200px;height:60px}
.headline{left:210px;top:160px;color:var(--white)}
.headline .thin{font-weight:200;font-size:54px;line-height:56px;letter-spacing:-4px}
.headline .bold{font-weight:800;font-size:66px;line-height:62px;letter-spacing:-.5px}
.headline .sub{font-weight:600;font-size:21px;line-height:25px;margin-top:4px}

.lead-card{left:763px;top:104px;width:223px;height:300px;background:linear-gradient(180deg,#1e6fb0,#2c86c6);border:3px solid #3a94d4;text-align:center;color:var(--white);padding:10px 14px}
.lead-card h2{font-family:"Oswald",Impact,sans-serif;font-weight:500;font-size:25px;line-height:30px;letter-spacing:.3px}
.lead-card p{font-size:11.5px;line-height:14px;margin-top:2px}
.mail-dot{width:22px;height:22px;border-radius:50%;background:var(--blue-dark);margin:8px auto 8px;display:flex;align-items:center;justify-content:center}
.field{display:block;width:178px;height:30px;margin:0 auto 5px;background:var(--white);border:1px solid #cfd8e0;font-size:10px;color:#777;text-align:left;padding:9px 8px;font-family:"Open Sans",Arial,sans-serif}
.req{font-size:10px;margin:6px 0 10px}
.btn{display:inline-block;background:var(--orange);color:var(--white);font-weight:700;text-transform:uppercase}
.lead-card .btn{width:178px;height:30px;line-height:30px;font-size:11px;background:var(--blue-dark);color:var(--orange)}

/* why */
.section-title{width:1200px;left:0;text-align:center;font-weight:500;font-size:27px;color:#2a2a2a}
.divider{left:513px;width:174px;height:24px}
.benefit{width:120px;text-align:center;font-size:11.5px;line-height:15px;color:#444}
.benefit .circle{width:80px;height:80px;border-radius:50%;margin:0 auto 14px;display:flex;align-items:center;justify-content:center}

/* imagine */
.imagine{left:0;top:842px;width:1200px;height:372px;background:linear-gradient(90deg,#1470c0 0%,#0f62ad 60%,#0c4d8c 100%)}
.imagine-copy{left:209px;top:892px;width:365px;color:var(--white)}
.imagine-copy h2{font-weight:700;font-size:25px;letter-spacing:.5px}
.imagine-copy .rule{width:52px;height:2px;background:var(--white);margin:8px 0 14px}
.imagine-copy p{font-size:11px;line-height:14.5px;margin-bottom:13px}
.collage{left:615px;top:900px;width:340px;height:314px;background:linear-gradient(135deg,#2a5a8a,#6b3a5a 50%,#1c3a5c);border-radius:4px}

/* how */
.how{left:0;top:1214px;width:1200px;height:380px;background:var(--light-bg)}
.how-copy{left:296px;top:1355px;width:608px;text-align:center;font-size:11px;line-height:15.5px;color:var(--muted)}
.how-copy p{margin-bottom:15px}
.how-btn{left:507px;top:1492px;width:186px;height:39px;line-height:39px;text-align:center;font-size:14px;font-weight:500;border-bottom:2px solid var(--orange-dark)}

/* testimonial */
.testimonial{left:0;top:1594px;width:1200px;height:380px;background:linear-gradient(135deg,#1a2433 0%,#2b3a4e 50%,#1c2636 100%)}
.quote-icon{left:566px;top:1660px;width:68px;height:68px}
.quote{left:322px;top:1770px;width:556px;text-align:center;color:var(--white);font-size:11.5px;line-height:17px}
.author{left:0;width:1200px;text-align:center;font-size:12px}
.author.name{top:1878px;color:var(--blue-light);font-weight:700}
.author.place{top:1894px;color:var(--white)}

/* bottom cta */
.cta{left:0;top:1974px;width:1200px;height:216px;background:var(--blue)}
.cta-title{left:0;top:2020px;width:1200px;text-align:center;color:var(--white);font-weight:700;font-size:27px}
.cta-sub{left:0;top:2057px;width:1200px;text-align:center;color:var(--white);font-size:12px}
.cta-field{top:2089px;height:39px;background:var(--white);font-family:"Open Sans",Arial,sans-serif;font-size:12px;color:#888;padding:12px 10px}
.cta-btn{left:825px;top:2089px;width:152px;height:39px;line-height:39px;text-align:center;font-size:12.5px;font-weight:600}

.footer{left:0;top:2190px;width:1200px;height:46px;background:var(--navy-deep);color:#8a96a6;font-size:9.5px;text-align:center;line-height:46px}
</style>
</head>
<body>

<header class="abs topbar"></header>
<div class="abs brand"><span class="brand-mark"></span>Bright Oak Promos</div>
<div class="abs contact">
  <svg width="20" height="20" viewBox="0 0 24 24" aria-hidden="true"><path fill="#fff" d="M6.6 10.8a15 15 0 0 0 6.6 6.6l2.2-2.2c.3-.3.7-.4 1-.2 1.1.4 2.3.6 3.6.6.6 0 1 .4 1 1V20c0 .6-.4 1-1 1A17 17 0 0 1 3 4c0-.6.4-1 1-1h3.5c.6 0 1 .4 1 1 0 1.3.2 2.5.6 3.6.1.3 0 .7-.2 1z"/></svg>
  <div>Usa Office: <strong>555-210-4471</strong><br>International: 1-800-555-0142</div>
</div>

<section class="abs hero" role="img" aria-label="Night skyline of a city with lit skyscrapers"></section>
<svg class="abs hero-curve" viewBox="0 0 1200 60" preserveAspectRatio="none" aria-hidden="true">
  <path d="M0 14 Q600 66 1200 14 V60 H0Z" fill="#fff"/>
</svg>

<div class="abs headline">
  <div class="thin">ATTRACT MORE</div>
  <div class="bold">CUSTOMER</div>
  <div class="sub">Who spend more money with your<br>business more often!</div>
</div>

<form class="abs lead-card" id="lead-form">
  <h2>ENTER YOUR INFO!</h2>
  <p>To be forwarded to our website for all the details and to receive samples in your email!</p>
  <div class="mail-dot"><svg width="12" height="9" viewBox="0 0 12 9" aria-hidden="true"><rect width="12" height="9" rx="1" fill="#fff"/><path d="M0 0 6 5 12 0" stroke="#0b4f91" fill="none"/></svg></div>
  <span class="field">Name</span>
  <span class="field">Email</span>
  <span class="field">Phone</span>
  <div class="req">*Mandatory Fiels</div>
  <span class="btn">Email me samples</span>
</form>

<h2 class="abs section-title" style="top:532px">Why Offer Incentives To Customers?</h2>
<svg class="abs divider" style="top:578px" viewBox="0 0 174 24" aria-hidden="true"><line x1="0" y1="12" x2="174" y2="12" stroke="#bbb"/><circle cx="87" cy="12" r="12" fill="#1570bf"/></svg>

<div class="abs benefit" style="left:201px;top:641px"><div class="circle" style="background:#1a6fc0"><svg width="38" height="38" viewBox="0 0 38 38" aria-hidden="true"><g fill="#fff"><rect x="4" y="26" width="5" height="8"/><rect x="12" y="21" width="5" height="13"/><rect x="20" y="16" width="5" height="18"/><rect x="28" y="10" width="5" height="24"/></g><path d="M4 20 14 12 20 15 32 4" stroke="#fff" stroke-width="2" fill="none"/></svg></div>Increase Responses From Your Existing Ads</div>
<div class="abs benefit" style="left:332px;top:641px"><div class="circle" style="background:#19b6c8"><svg width="36" height="36" viewBox="0 0 36 36" aria-hidden="true"><path d="M6 30 26 10M10 6 30 26" stroke="#fff" stroke-width="5" stroke-linecap="round"/></svg></div>#1 Sales Closing Tool - Gift w/Purchase</div>
<div class="abs benefit" style="left:465px;top:641px"><div class="circle" style="background:#8cc21f"><svg width="36" height="36" viewBox="0 0 36 36" aria-hidden="true"><circle cx="18" cy="14" r="10" fill="none" stroke="#fff" stroke-width="3"/><path d="M12 22 9 34 18 29 27 34 24 22" fill="#fff"/></svg></div>Build Brand Awareness and Trust</div>
<div class="abs benefit" style="left:599px;top:641px"><div class="circle" style="background:#f5a50d"><svg width="38" height="34" viewBox="0 0 38 34" aria-hidden="true"><g fill="#fff"><circle cx="19" cy="9" r="5"/><circle cx="8" cy="12" r="4"/><circle cx="30" cy="12" r="4"/><path d="M10 28c0-7 18-7 18 0zM1 28c0-6 10-6 10-2v2zM37 28c0-6-10-6-10-2v2z"/></g></svg></div>Insure The Sale Over Your Competition</div>
<div class="abs benefit" style="left:733px;top:641px"><div class="circle" style="background:#55d3a6"><svg width="36" height="36" viewBox="0 0 36 36" aria-hidden="true"><g fill="none" stroke="#fff" stroke-width="4" stroke-dasharray="4 3"><circle cx="14" cy="20" r="9"/><circle cx="27" cy="9" r="5"/></g></svg></div>Boost Repeat and Referral Business</div>
<div class="abs benefit" style="left:874px;top:641px"><div class="circle" style="background:#e9669e"><svg width="34" height="34" viewBox="0 0 34 34" aria-hidden="true"><path d="M4 4h12l14 14-12 12L4 16z" fill="none" stroke="#fff" stroke-width="3"/><circle cx="11" cy="11" r="2.5" fill="#fff"/></svg></div>Improve Retention Rates</div>

<section class="abs imagine"></section>
<div class="abs imagine-copy">
  <h2>IMAGINE</h2>
  <div class="rule"></div>
  <p>Being able to create exciting give away promotions that will boost your sales without ever having to worry about cost.</p>
  <p>Bright Oak Promo Group, Inc. provides high-perceived value promotional incentives to businesses that want to advertise an exciting Give Away that will instantly attract more customers from your existing advertising efforts.</p>
  <p>Your business can give away incentive certificates that are redeemable for luxury hotel &amp; resort stays with airfare included, cruises, cash for gas, groceries, dining and even electronic goods.</p>
</div>
<div class="abs collage" role="img" aria-label="Fanned stack of printed incentive certificates for cruises, hotel stays, cash back rewards and electronics"></div>

<section class="abs how"></section>
<h2 class="abs section-title" style="top:1264px;font-weight:400">How Can We Do It</h2>
<svg class="abs divider" style="top:1310px" viewBox="0 0 174 24" aria-hidden="true"><line x1="0" y1="12" x2="174" y2="12" stroke="#bbb"/><circle cx="87" cy="12" r="12" fill="#1570bf"/></svg>
<div class="abs how-copy">
  <p>We help fill empty rooms for thousands of hotels and resorts in hundreds of destinations around the world as well as the major cruise lines. Hotels and resorts are rarely full so when we place someone in their empty rooms, they end up making it up when travelers spend money on room service, spa services, eat at their in-house restaurants, casino and take advantage of other amenities that drive revenue.</p>
  <p>We also help over 18,000 restaurants, electronic manufacturers, the major gas companies and top grocery chains in the U.S and Canada increase brand awareness as well as increase customer loyalty.</p>
</div>
<a class="abs btn how-btn" href="#lead-form">DOWNLOAD SAMPLES</a>

<section class="abs testimonial" role="img" aria-label="Dim photo of hands working at a laptop on a desk"></section>
<svg class="abs quote-icon" viewBox="0 0 68 68" aria-hidden="true"><circle cx="34" cy="34" r="32" fill="#1570bf" stroke="#fff" stroke-width="4"/><path d="M20 24h18v12H27l-5 4v-4h-2z" fill="#fff"/><path d="M40 30h8v12h-2v4l-5-4h-11v-4h10z" fill="#fff"/></svg>
<p class="abs quote">"I began using your incentives two years ago to boost lead generation efforts. I have experienced a 63% increase in lead captures. And, even more importantly, my sales have increased as well. The ability to offer unlimited certificates and not having to pay for each certificate I give away is perhaps the best feature of the program, but having the flexibility to email or print certificates for my customers is also wonderful. I even use your html banners to automate my promotions right on my website!. "</p>
<div class="abs author name">Dan R</div>
<div class="abs author place">Cedar Falls, TN</div>

<section class="abs cta"></section>
<h2 class="abs cta-title">ENTER YOUR INFO!</h2>
<p class="abs cta-sub">To be forwarded to our website for all the details and to receive samples in your email!</p>
<span class="abs cta-field" style="left:220px;width:199px">Name*</span>
<span class="abs cta-field" style="left:422px;width:198px">Email*</span>
<span class="abs cta-field" style="left:624px;width:197px">Phone*</span>
<span class="abs btn cta-btn">EMAIL ME SAMPLES</span>

<footer class="abs footer">Copyright 2017 © Bright Oak Promo Group, Inc. All Rights Reserved .</footer>
</body>
</html>
```